KWM Plumbing and Roofing

design a fresh modern card for a young plumbing business looking to break into the market.
Must include the logo in the attached file
Lowen Fairbrook
Phone number 0412689405
Vic Licence no 63920
email......

New Homes & Renovations
General Plumbing & Maintenance
Solar Hot Water Units
Roofing & Guttering (new and replacement)

Industry/Entity Type

Business

```html
<!DOCTYPE html>
<html lang="en">
<head>
<meta charset="utf-8">
<title>KWM Plumbing and Roofing – Stationery</title>
<link rel="stylesheet" href="https://fonts.googleapis.com/css2?family=Arimo:wght@400;700&display=swap">
<style>
  :root {
    --backdrop: #ececec;
    --paper: #ffffff;
    --navy: #0b5077;
    --gold-dark: #c08a1e;
    --gold-light: #f3d37a;
    --ink: #1d1d1d;
    --on-navy: #ffffff;
    --mark-faint: #e6eef2;
  }
  * { box-sizing: border-box; margin: 0; padding: 0; }
  html, body { width: 1200px; height: 957px; overflow: hidden; }
  body {
    background: var(--backdrop);
    font-family: "Arimo", Arial, sans-serif;
    color: var(--ink);
    position: relative;
  }
  .sheet { position: absolute; background: var(--paper); overflow: hidden; }

  .gold-band {
    background: linear-gradient(90deg, var(--gold-dark) 0%, var(--gold-light) 55%, var(--gold-dark) 100%);
  }

  .wordmark {
    display: flex; align-items: center; gap: 10px;
    color: var(--navy); font-weight: 700; position: absolute;
  }
  .wordmark .dot { border-radius: 50%; background: var(--navy); flex: none; }

  /* Business card – back */
  .card-back { left: 32px; top: 75px; width: 425px; height: 243px; }
  .card-back .wordmark { left: 38px; top: 52px; font-size: 17px; }
  .card-back .wordmark .dot { width: 34px; height: 34px; }
  .card-back .name-band {
    position: absolute; left: 0; top: 126px; width: 100%; height: 30px;
    color: var(--on-navy); font-size: 16px; text-align: right;
    padding-right: 18px; line-height: 30px;
  }
  .card-back .contact-band {
    position: absolute; left: 0; top: 156px; width: 100%; height: 87px;
    background: var(--navy); color: var(--on-navy);
  }
  .contact-list { list-style: none; }
  .contact-list li { display: flex; align-items: center; gap: 8px; }
  .contact-list svg { width: 12px; height: 12px; flex: none; }
  .card-back .contact-list { position: absolute; left: 34px; top: 14px; font-size: 13px; }
  .card-back .contact-list li { height: 22px; }
  .licence { position: absolute; right: 15px; bottom: 14px; font-size: 10px; }

  /* Business card – front */
  .card-front { left: 32px; top: 349px; width: 425px; height: 242px; }
  .card-front .wordmark { left: 100px; top: 98px; font-size: 21px; }
  .card-front .wordmark .dot { width: 44px; height: 44px; }
  .card-front .gold-band { position: absolute; left: 0; bottom: 0; width: 100%; height: 13px; }

  /* Letterhead */
  .letterhead { left: 514px; top: 66px; width: 636px; height: 807px; }
  .letterhead .wordmark { left: 44px; top: 36px; font-size: 14px; }
  .letterhead .wordmark .dot { width: 30px; height: 30px; }
  .letterhead .contact-list { position: absolute; left: 427px; top: 24px; font-size: 11px; }
  .letterhead .contact-list li { height: 19px; }
  .letterhead .contact-list svg { width: 10px; height: 10px; }
  .letterhead .rule {
    position: absolute; left: 206px; top: 83px; width: 372px; height: 2px;
    background: linear-gradient(90deg, rgba(192,138,30,0) 0%, var(--gold-dark) 30%, var(--gold-light) 80%, rgba(243,211,122,0) 100%);
  }
  .letterhead .faint-mark {
    position: absolute; left: 228px; top: 300px; width: 180px; height: 180px;
    border-radius: 50%; background: var(--mark-faint);
  }
  .letterhead .footer-band {
    position: absolute; left: 0; bottom: 0; width: 100%; height: 38px; background: var(--navy);
  }
</style>
</head>
<body>

<svg width="0" height="0" style="position:absolute" aria-hidden="true">
  <defs>
    <symbol id="icon-phone" viewBox="0 0 12 12">
      <path d="M3 1 C5 2 5 3 4.5 4 L4 5 C4.5 6.5 5.5 7.5 7 8 L8 7.5 C9 7 10 7 11 9 L10 11 C5 11 1 7 1 2 Z" fill="currentColor"/>
    </symbol>
    <symbol id="icon-fax" viewBox="0 0 12 12">
      <rect x="3" y="1" width="6" height="4" fill="none" stroke="currentColor"/>
      <rect x="1" y="5" width="10" height="4" fill="none" stroke="currentColor"/>
      <rect x="3" y="8" width="6" height="3" fill="none" stroke="currentColor"/>
    </symbol>
    <symbol id="icon-mail" viewBox="0 0 12 12">
      <rect x="0.5" y="2.5" width="11" height="7" fill="none" stroke="currentColor"/>
      <path d="M0.5 2.5 L6 7 L11.5 2.5" fill="none" stroke="currentColor"/>
    </symbol>
  </defs>
</svg>

<section class="sheet card-back">
  <div class="wordmark"><span class="dot"></span>KWM Plumbing and Roofing</div>
  <div class="name-band gold-band">Lowen Fairbrook</div>
  <div class="contact-band">
    <ul class="contact-list">
      <li><svg><use href="#icon-phone"/></svg>0412 689405</li>
      <li><svg><use href="#icon-fax"/></svg>+(000) 1234 5678</li>
      <li><svg><use href="#icon-mail"/></svg>name@emailaddress.com</li>
    </ul>
    <span class="licence">Licence no 63920</span>
  </div>
</section>

<section class="sheet card-front">
  <div class="wordmark"><span class="dot"></span>KWM Plumbing and Roofing</div>
  <div class="gold-band"></div>
</section>

<section class="sheet letterhead">
  <div class="wordmark"><span class="dot"></span>KWM Plumbing and Roofing</div>
  <ul class="contact-list">
    <li><svg><use href="#icon-phone"/></svg>0412 689405</li>
    <li><svg><use href="#icon-fax"/></svg>+(000) 1234 5678</li>
    <li><svg><use href="#icon-mail"/></svg>name@emailaddress.com</li>
  </ul>
  <div class="rule"></div>
  <div class="faint-mark"></div>
  <div class="footer-band"></div>
</section>

</body>
</html>
```